Brochure to attract insurance agents to outsource their bookkeeping

I need a brochure to handout at trade shows. Company name is Corvant Producer Ledger & Records. We go by CPLR. We provide bookkeeping services. I have attached the current brochure, which is a few years old, stale and outdated (not created on PixelGrove). I have also attached our graphic identity manual which show fonts/colors as well as our logo in 3 styles

Target Market(s)

Insurance Agents needing bookkeeping services

Industry/Entity Type

Accounting

Other font styles liked:
• See the graphic id manual

Colors
00AB8E
00BBA5
67D7C9
C6EFE9
E9F9F6

Requirements
Must have
• Services noted (see current brochure), contact info, reference to Brantwell Orbit

```html
<!DOCTYPE html>
<html lang="en">
<head>
<meta charset="utf-8">
<title>CPLR Tri-Fold Brochure</title>
<link href="https://fonts.googleapis.com/css2?family=Montserrat:wght@300;400;500;600;700;800&family=Oswald:wght@400;500&display=swap" rel="stylesheet">
<style>
:root{
  --teal:#00AB8E;
  --teal-2:#00BBA5;
  --teal-3:#67D7C9;
  --teal-4:#C6EFE9;
  --teal-5:#E9F9F6;
  --teal-deep:#0d8b80;
  --ink:#2b2b2b;
  --grey:#5c5c5c;
  --grey-light:#d9d9d9;
  --panel-fill:#e6e8f3;
  --white:#ffffff;
}
*{box-sizing:border-box;margin:0;padding:0}
html,body{width:1200px;height:2232px;overflow:hidden;background:var(--white)}
body{position:relative;font-family:'Montserrat',sans-serif;color:var(--ink)}
.abs{position:absolute}
.spread{position:absolute;left:98px;width:1003px;height:780px;box-shadow:0 2px 8px rgba(0,0,0,.25);overflow:hidden}
.spread--outer{top:83px}
.spread--inner{top:887px}
.panel{position:absolute;top:0;width:334px;height:780px;overflow:hidden}
.panel--a{left:0}.panel--b{left:334px}.panel--c{left:669px}
.panel--white{background:var(--white)}
.panel--teal{background:linear-gradient(160deg,#12a596 0%,var(--teal-deep) 55%,#0b7d73 100%)}
.foot{position:absolute;left:0;bottom:25px;width:100%;height:21px;background:var(--white);font-weight:700;font-size:10.5px;text-align:center;line-height:21px;color:var(--ink);letter-spacing:.1px}
.foot--teal{color:var(--teal)}
.foot-base{position:absolute;left:0;bottom:0;width:100%;height:25px;background:linear-gradient(#b8b8b8,#8d8d8d)}
.foot-base--teal{background:var(--teal-deep)}
.tab{position:absolute;height:42px;font-family:'Oswald',sans-serif;font-size:17px;line-height:42px;padding:0 22px 0 24px;border-radius:0 21px 21px 0;letter-spacing:.1px;white-space:nowrap}
.tab--white{background:var(--white);color:var(--teal)}
.tab--teal{background:linear-gradient(90deg,var(--teal),var(--teal-2));color:var(--white)}
.photo{position:absolute}
/* outer flap */
.contact{position:absolute;left:0;top:55px;width:334px;text-align:center}
.contact h2{font-size:21px;font-weight:500;letter-spacing:.5px;color:var(--ink)}
.contact h2 span{color:var(--teal)}
.cicon{display:block;margin:4px auto 3px;width:19px;height:19px}
.contact p{font-size:10.5px;font-weight:500;line-height:13px}
.contact .phone{font-size:16px;font-weight:500}
.contact .small{font-size:8.5px}
.mission{position:absolute;left:24px;top:316px;width:286px;font-size:12.2px;line-height:15px;text-align:justify;text-align-last:center}
.promise{position:absolute;left:0;top:550px;width:334px;text-align:center}
.promise .l1{font-size:27px;font-weight:800;color:var(--grey);line-height:28px}
.promise .l2{font-size:15px;font-weight:800;color:#8a8a8a;line-height:17px;display:inline-block;border-bottom:1.5px solid var(--teal);padding:0 28px 1px}
.promise .l3{font-size:18px;font-weight:800;color:var(--teal);line-height:20px;margin-top:2px}
.promise .l4{font-size:32px;font-weight:800;color:var(--teal);line-height:30px}
/* team */
.member{position:absolute;width:150px;text-align:center;color:var(--white);font-size:10px;font-weight:600;line-height:12px}
.head{position:absolute;width:108px;height:108px;border-radius:50%;border:5px solid var(--white);background:radial-gradient(circle at 50% 40%,#8e8e8e,#4a4a4a 75%)}
.ring{position:absolute;width:126px;height:126px;border-radius:50%;border:4px solid var(--white);border-right-color:transparent;transform:rotate(40deg)}
.staff-note{position:absolute;left:0;top:652px;width:334px;text-align:center;color:var(--white);font-family:'Oswald',sans-serif}
.staff-note .big{font-size:21px;line-height:24px}
.staff-note .sm{font-size:11.5px;line-height:14px}
.staff-note .sm span{color:var(--teal-3)}
/* front */
.brand{position:absolute;left:14px;top:50px;color:var(--teal);font-weight:800}
.brand .mark{display:inline-block;width:14px;height:14px;background:var(--teal);vertical-align:middle;margin-right:6px}
.brand .abbr{font-size:36px;vertical-align:middle;letter-spacing:1px}
.brand .full{display:block;font-size:7.5px;letter-spacing:.2px;margin-top:2px}
.feat{position:absolute;border-radius:50%;background:var(--white);border:3px solid #e0e0e0;box-shadow:0 2px 6px rgba(0,0,0,.25);display:flex;align-items:center;justify-content:center}
.feat-label{position:absolute;font-size:8px;font-weight:700;color:var(--ink);white-space:nowrap}
.hero{position:absolute;right:23px;top:549px;text-align:right;line-height:27px;white-space:nowrap}
.hero .h1{font-size:26px;font-weight:400;color:var(--ink)}
.hero .h2{font-size:25px;font-weight:700;color:var(--grey)}
.hero .h3{font-size:27px;font-weight:700;color:var(--teal)}
.tagline{position:absolute;right:23px;top:686px;text-align:right;color:var(--white);font-size:8.5px;font-weight:600;line-height:11px}
/* how it works */
.intro{position:absolute;left:24px;top:88px;width:279px;font-size:10.8px;font-weight:300;color:var(--white);line-height:13.2px;text-align:justify}
.steps{position:absolute;left:30px;top:172px;width:274px;list-style:none;color:var(--white);font-size:10.6px;font-weight:500;line-height:13px;display:flex;flex-direction:column;gap:12px}
.steps li{position:relative;margin-left:22px;width:252px}
.steps li.j{text-align:justify}
.tick{position:absolute;left:-22px;top:0;width:12px;height:12px}
.steps-line{position:absolute;left:38px;top:188px;width:1px;height:420px;background:rgba(255,255,255,.6)}
.call{position:absolute;left:43px;top:650px;display:flex;align-items:center;color:var(--white);font-size:27px;font-weight:500}
.call svg{margin-right:12px}
.call-rule{position:absolute;left:118px;top:711px;width:91px;height:1px;background:rgba(255,255,255,.8)}
/* services */
.svc{position:absolute;width:140px;text-align:center}
.svc-icon{width:84px;height:84px;margin:0 auto;border-radius:50%;background:radial-gradient(circle at 50% 40%,var(--teal-2),var(--teal-deep));border:4px solid var(--white);box-shadow:0 0 0 1px #cfcfcf,0 3px 6px rgba(0,0,0,.25);display:flex;align-items:center;justify-content:center}
.svc-name{margin-top:8px;font-size:9px;font-weight:700;line-height:11px;color:var(--ink)}
/* fees */
.fees-body{position:absolute;left:22px;top:88px;width:290px}
.fees-text{color:var(--white);font-size:9.9px;font-weight:600;line-height:12.6px;text-align:justify}
.fee-table{margin:10px 0 0 22px;width:235px;border:1px solid rgba(255,255,255,.8);border-radius:0 0 10px 10px;border-collapse:separate;border-spacing:0;color:var(--white);font-size:11.5px;line-height:13.2px;overflow:hidden}
.fee-table th{background:#eaeaea;color:#5a5a5a;font-weight:500;text-align:left;font-size:10px;line-height:13px;padding:6px}
.fee-table td{padding:0 6px}
.fee-table tbody tr:first-child td{padding-top:8px}
.fee-table tbody tr:last-child td{padding-bottom:8px}
.fees-more{margin:16px auto 0;width:274px;text-align:center;color:var(--white);font-size:13px;font-weight:700;line-height:16px}
/* panel map */
.map-title{position:absolute;left:0;top:1789px;width:1109px;text-align:center;font-size:25px;font-weight:700;color:#333}
.map{position:absolute;top:1853px;width:372px;height:257px;background:var(--panel-fill);border:2px solid #9a9a9a;display:flex}
.map div{flex:1;display:flex;align-items:center;justify-content:center;text-align:center;font-size:16px;font-weight:700;line-height:23px;color:#333}
.map div+div{border-left:1px dashed #8d8d8d}
</style>
</head>
<body>

<section class="spread spread--outer">

  <div class="panel panel--a panel--white">
    <div class="photo" role="img" aria-label="Desk with business cards and stationery" style="left:0;top:0;width:334px;height:300px;background:linear-gradient(120deg,#ffffff 35%,#e4e4e4 70%,#cfcfcf 100%)"></div>
    <div class="contact">
      <h2>GET IN <span>TOUCH</span></h2>
      <svg class="cicon" viewBox="0 0 20 20"><circle cx="10" cy="10" r="10" fill="#00AB8E"/><path d="M10 4.5a3.5 3.5 0 0 0-3.5 3.5c0 2.6 3.5 7 3.5 7s3.5-4.4 3.5-7A3.5 3.5 0 0 0 10 4.5zm0 5a1.5 1.5 0 1 1 0-3 1.5 1.5 0 0 1 0 3z" fill="#fff"/></svg>
      <p>47 ALDER MILL ROAD<br>FENWICK, CT 06020</p>
      <svg class="cicon" viewBox="0 0 20 20"><circle cx="10" cy="10" r="10" fill="#00AB8E"/><path d="M7 5l2 2.5-1 1.3c.6 1.3 1.7 2.4 3 3l1.3-1L15 12.8l-1.2 1.6c-3.6-.3-7.4-4.1-7.7-7.7z" fill="#fff"/></svg>
      <p class="phone">555.201.4477</p>
      <svg class="cicon" viewBox="0 0 20 20"><circle cx="10" cy="10" r="10" fill="#00AB8E"/><rect x="5" y="6.5" width="10" height="7" fill="#fff"/><path d="M5 6.5l5 4 5-4" stroke="#00AB8E" fill="none"/></svg>
      <p class="small">DANA@CPLRLEDGER.COM</p>
      <svg class="cicon" viewBox="0 0 20 20"><circle cx="10" cy="10" r="10" fill="#00AB8E"/><circle cx="10" cy="10" r="5" fill="none" stroke="#fff"/><path d="M5 10h10M10 5c-2 3-2 7 0 10M10 5c2 3 2 7 0 10" stroke="#fff" fill="none"/></svg>
      <p class="small" style="margin-top:6px">WWW.PRODUCERLEDGERBOOKS.COM</p>
    </div>
    <div class="tab tab--teal" style="left:0;top:261px">CPLR MISSION STATEMENT</div>
    <p class="mission">CPLR’s mission is to provide Independent Insurance Agencies a resource to have their accounting and bookkeeping performed accurately, timely, and cost effectively. CPLR offers it’s clients an assigned team consisting of a bookkeeper, clerk, and accountant.</p>
    <div class="photo" role="img" aria-label="Hand using a desk calculator" style="left:0;top:420px;width:310px;height:120px;background:linear-gradient(100deg,#f3f3f3,#dcdcdc 55%,#eeeeee)"></div>
    <div class="promise">
      <div class="l1">HAVE CPLR BE</div>
      <div class="l2">AN INTEGRAL PART OF</div>
      <div class="l3">YOUR AGENCY’S</div>
      <div class="l4">SUCCESS</div>
    </div>
    <svg class="abs" style="left:0;top:620px" width="334" height="115" viewBox="0 0 334 115"><path d="M0 95 Q170 130 334 75 V115 H0Z" fill="#9c9c9c"/><path d="M0 0 Q10 60 0 95 Z" fill="#b0b0b0"/></svg>
    <div class="foot">WWW.PRODUCERLEDGERBOOKS.COM</div>
    <div class="foot-base"></div>
  </div>

  <div class="panel panel--b panel--teal">
    <div class="tab tab--white" style="left:0;top:47px">CPLR MANAGEMENT TEAM</div>

    <div class="ring" style="left:31px;top:131px"></div>
    <div class="head" role="img" aria-label="Portrait of Dana Whitcombe" style="left:40px;top:140px"></div>
    <div class="member" style="left:19px;top:262px">Dana Whitcombe<br>President</div>
    <div class="ring" style="left:174px;top:131px"></div>
    <div class="head" role="img" aria-label="Portrait of Owen Pratley" style="left:183px;top:140px"></div>
    <div class="member" style="left:162px;top:262px">Owen Pratley<br>Director of Accounting</div>

    <div class="ring" style="left:31px;top:302px"></div>
    <div class="head" role="img" aria-label="Portrait of Leah Corbin" style="left:40px;top:311px"></div>
    <div class="member" style="left:19px;top:433px">Leah Corbin<br>Manager</div>
    <div class="ring" style="left:174px;top:302px"></div>
    <div class="head" role="img" aria-label="Portrait of Marcus Tellwyn" style="left:183px;top:311px"></div>
    <div class="member" style="left:162px;top:433px">Marcus Tellwyn<br>Manager</div>

    <div class="ring" style="left:31px;top:478px"></div>
    <div class="head" role="img" aria-label="Portrait of Nora Haskett" style="left:40px;top:487px"></div>
    <div class="member" style="left:19px;top:609px">Nora Haskett<br>Manager</div>
    <div class="ring" style="left:174px;top:478px"></div>
    <div class="head" role="img" aria-label="Portrait of Eli Brandmoor" style="left:183px;top:487px"></div>
    <div class="member" style="left:162px;top:609px">Eli Brandmoor<br>Manager</div>

    <div class="staff-note">
      <div class="big">FOR A COMPLETE LIST OF CPLR STAFF</div>
      <div class="sm">PLEASE VISIT <span>WWW.PRODUCERLEDGERBOOKS.COM</span></div>
    </div>
    <svg class="abs" style="left:0;top:690px" width="334" height="45" viewBox="0 0 334 45"><path d="M0 40 Q170 45 334 0 V45 H0Z" fill="#0a6f66"/></svg>
    <div class="foot foot--teal">WWW.PRODUCERLEDGERBOOKS.COM</div>
    <div class="foot-base"></div>
  </div>

  <div class="panel panel--c panel--white">
    <div class="photo" role="img" aria-label="Soft grey backdrop" style="left:0;top:0;width:334px;height:40px;background:linear-gradient(90deg,#fff,#d6d6d6)"></div>
    <div class="brand"><span class="mark"></span><span class="abbr">CPLR</span><span class="full">CORVANT PRODUCER LEDGER &amp; RECORDS</span></div>
    <div class="photo" role="img" aria-label="Laptop with financial charts, calculator and pen on a desk" style="left:105px;top:130px;width:290px;height:380px;border-radius:50%;background:radial-gradient(circle at 45% 45%,#f4f4f4,#b9bec4 60%,#5f6770)"></div>
    <svg class="abs" style="left:70px;top:110px" width="264" height="430" viewBox="0 0 264 430"><path d="M264 12 A200 200 0 0 0 60 205 A200 200 0 0 0 264 410" fill="none" stroke="#00BBA5" stroke-width="6"/><path d="M264 2 A215 215 0 0 0 45 205" fill="none" stroke="#C6EFE9" stroke-width="10"/></svg>

    <div class="feat" style="left:58px;top:170px;width:72px;height:72px"><svg width="36" height="36" viewBox="0 0 36 36"><ellipse cx="16" cy="9" rx="10" ry="4" fill="none" stroke="#00AB8E" stroke-width="2"/><path d="M6 9v16c0 2 4 4 10 4M26 9v8M6 17c0 2 4 4 10 4" fill="none" stroke="#00AB8E" stroke-width="2"/><circle cx="27" cy="26" r="6" fill="#00AB8E"/><path d="M24 26l2 2 4-4" stroke="#fff" stroke-width="1.6" fill="none"/></svg></div>
    <div class="feat-label" style="left:23px;top:252px">DATA SECURITY</div>
    <div class="feat" style="left:24px;top:273px;width:82px;height:82px"><svg width="44" height="44" viewBox="0 0 44 44"><path d="M22 3l5 4 6-1 1 6 5 4-3 6 3 6-5 4-1 6-6-1-5 4-5-4-6 1-1-6-5-4 3-6-3-6 5-4 1-6 6 1z" fill="#00AB8E"/><circle cx="22" cy="22" r="9" fill="none" stroke="#fff" stroke-width="2"/><path d="M18 22l3 3 5-6" stroke="#fff" stroke-width="2" fill="none"/></svg></div>
    <div class="feat-label" style="left:23px;top:365px">QUALITY CONTROL</div>
    <div class="feat" style="left:72px;top:378px;width:100px;height:100px"><svg width="52" height="52" viewBox="0 0 52 52"><circle cx="26" cy="26" r="8" fill="none" stroke="#00AB8E" stroke-width="2.5"/><circle cx="26" cy="26" r="13" fill="none" stroke="#00AB8E" stroke-width="2.5" stroke-dasharray="5 3"/><path d="M8 22a19 19 0 0 1 32-10M44 30a19 19 0 0 1-32 10" fill="none" stroke="#00AB8E" stroke-width="2.5"/></svg></div>
    <div class="feat-label" style="left:45px;top:492px">CONTINUITY OF SERVICE</div>
    <div class="feat" style="left:197px;top:405px;width:108px;height:108px"><svg width="60" height="40" viewBox="0 0 60 40"><circle cx="30" cy="10" r="6" fill="#00AB8E"/><path d="M19 34c0-8 5-13 11-13s11 5 11 13z" fill="#00AB8E"/><circle cx="13" cy="16" r="5" fill="#00BBA5"/><path d="M4 36c0-7 4-11 9-11s9 4 9 11z" fill="#00BBA5"/><circle cx="47" cy="16" r="5" fill="#00BBA5"/><path d="M38 36c0-7 4-11 9-11s9 4 9 11z" fill="#00BBA5"/></svg></div>
    <div class="feat-label" style="left:149px;top:523px">EDUCATED &amp; TRAINED STAFF</div>

    <div class="hero">
      <div class="h1">NEED HELP WITH</div>
      <div class="h2">BRANTWELL ORBIT<sup style="font-size:12px;font-weight:400">®</sup></div>
      <div class="h3">ACCOUNTING?</div>
    </div>
    <svg class="abs" style="left:0;top:640px" width="334" height="95" viewBox="0 0 334 95"><path d="M0 95 Q150 60 334 10 V95Z" fill="#a3a3a3"/><path d="M0 95 Q150 50 334 0 V12 Q150 62 0 95Z" fill="#00AB8E"/></svg>
    <div class="tagline">THE<br>LEADING<br>REMOTE BOOKKEEPING<br>FIRM FOR BRANTWELL ORBIT AGENCIES NATIONWIDE</div>
    <div class="foot">WWW.PRODUCERLEDGERBOOKS.COM</div>
    <div class="foot-base"></div>
  </div>
</section>

<section class="spread spread--inner">

  <div class="panel panel--a panel--teal">
    <div class="tab tab--white" style="left:0;top:24px">HOW OUTSOURCING TO CPLR WORKS</div>
    <p class="intro">We access your Brantwell Orbit online database in the same manner as Agency staff. You provide the login credentials. Below is a high-level overview of the process. A detailed operational workflow is provided to each client Agency.</p>
    <div class="steps-line"></div>
    <ul class="steps">
      <li><svg class="tick" viewBox="0 0 12 12"><circle cx="6" cy="6" r="6" fill="#fff"/><path d="M3.3 6.2l1.8 1.8 3.6-3.8" stroke="#0d8b80" stroke-width="1.5" fill="none"/></svg>Agency staff routes accounting documents to CPLR through Brantwell Orbit.</li>
      <li><svg class="tick" viewBox="0 0 12 12"><circle cx="6" cy="6" r="6" fill="#fff"/><path d="M3.3 6.2l1.8 1.8 3.6-3.8" stroke="#0d8b80" stroke-width="1.5" fill="none"/></svg>Agency staff makes bank deposits of paper checks and cash, routing documentation to CPLR to record in Brantwell Orbit. CPLR records EFT transactions from the bank records.</li>
      <li class="j"><svg class="tick" viewBox="0 0 12 12"><circle cx="6" cy="6" r="6" fill="#fff"/><path d="M3.3 6.2l1.8 1.8 3.6-3.8" stroke="#0d8b80" stroke-width="1.5" fill="none"/></svg>CPLR pays your agency bill premiums electronically when possible, or via Brantwell Orbit checks that you print. Agencies may choose the method.</li>
      <li class="j"><svg class="tick" viewBox="0 0 12 12"><circle cx="6" cy="6" r="6" fill="#fff"/><path d="M3.3 6.2l1.8 1.8 3.6-3.8" stroke="#0d8b80" stroke-width="1.5" fill="none"/></svg>CPLR reconciles Agency staff invoicing on all agency bill transactions with insurance company/broker records at time of payment. We work with your staff on discrepancies.</li>
      <li class="j"><svg class="tick" viewBox="0 0 12 12"><circle cx="6" cy="6" r="6" fill="#fff"/><path d="M3.3 6.2l1.8 1.8 3.6-3.8" stroke="#0d8b80" stroke-width="1.5" fill="none"/></svg>CPLR records all direct bill commission at the time commission is received; this includes downloads, imports, and manual entry. You provide the commission statements or provide online access for CPLR to obtain.</li>
      <li><svg class="tick" viewBox="0 0 12 12"><circle cx="6" cy="6" r="6" fill="#fff"/><path d="M3.3 6.2l1.8 1.8 3.6-3.8" stroke="#0d8b80" stroke-width="1.5" fill="none"/></svg>CPLR reconciles all bank accounts in Brantwell Orbit with your bank’s data at least twice per week. You provide the login credentials.</li>
      <li><svg class="tick" viewBox="0 0 12 12"><circle cx="6" cy="6" r="6" fill="#fff"/><path d="M3.3 6.2l1.8 1.8 3.6-3.8" stroke="#0d8b80" stroke-width="1.5" fill="none"/></svg>CPLR sends financial statements to Agency Principals each month. We encourage review and discussion.</li>
    </ul>
    <div class="call"><svg width="48" height="48" viewBox="0 0 48 48"><circle cx="24" cy="24" r="22" fill="none" stroke="#fff" stroke-width="2"/><path d="M16 13l5 6-2.4 3c1.5 3 4 5.5 7 7l3-2.4 6 5-2.8 3.6C23.5 34.5 14 25 13.4 16z" fill="none" stroke="#fff" stroke-width="2"/></svg>555.201.4477</div>
    <div class="call-rule"></div>
    <div class="foot">WWW.PRODUCERLEDGERBOOKS.COM</div>
    <div class="foot-base foot-base--teal"></div>
  </div>

  <div class="panel panel--b panel--white">
    <div class="tab tab--teal" style="left:0;top:24px">SERVICES AVAILABLE</div>
    <div class="svc" style="left:41px;top:104px"><div class="svc-icon"><svg width="40" height="40" viewBox="0 0 40 40"><rect x="12" y="8" width="18" height="12" rx="2" fill="#fff" transform="rotate(30 21 14)"/><path d="M6 30h10l8-4h10v6H6z" fill="#fff"/></svg></div><div class="svc-name">RECONCILE &amp; PAY<br>AGENCY BILL<br>PREMIUMS</div></div>
    <div class="svc" style="left:158px;top:104px"><div class="svc-icon"><svg width="40" height="40" viewBox="0 0 40 40"><circle cx="20" cy="8" r="5" fill="#fff"/><ellipse cx="20" cy="25" rx="13" ry="10" fill="#fff"/></svg></div><div class="svc-name">RECORD<br>DIRECT BILL<br>COMMISSION</div></div>
    <div class="svc" style="left:41px;top:253px"><div class="svc-icon"><svg width="40" height="40" viewBox="0 0 40 40"><rect x="9" y="5" width="22" height="30" rx="2" fill="none" stroke="#fff" stroke-width="2"/><path d="M13 12h14M13 18h14M13 24h9" stroke="#fff" stroke-width="2"/></svg></div><div class="svc-name">PAY VENDOR<br>INVOICES</div></div>
    <div class="svc" style="left:158px;top:253px"><div class="svc-icon"><svg width="40" height="40" viewBox="0 0 40 40"><rect x="7" y="12" width="26" height="20" rx="3" fill="none" stroke="#fff" stroke-width="2.2"/><rect x="24" y="19" width="9" height="6" fill="#fff"/><circle cx="20" cy="8" r="4" fill="#fff"/></svg></div><div class="svc-name" style="margin-top:16px">PROCESS PAYROLL</div></div>
    <div class="svc" style="left:41px;top:396px"><div class="svc-icon"><svg width="40" height="40" viewBox="0 0 40 40"><rect x="7" y="5" width="20" height="28" rx="2" fill="none" stroke="#fff" stroke-width="2"/><path d="M11 12h12M11 18h12" stroke="#fff" stroke-width="2"/><ellipse cx="29" cy="26" rx="6" ry="2.5" fill="#fff"/><rect x="23" y="26" width="12" height="8" fill="#fff"/></svg></div><div class="svc-name">RECORD DEPOSITS</div></div>
    <div class="svc" style="left:158px;top:396px"><div class="svc-icon"><svg width="40" height="40" viewBox="0 0 40 40"><rect x="7" y="5" width="22" height="30" rx="2" fill="none" stroke="#fff" stroke-width="2"/><path d="M12 16v-5M16 16v-7M20 16v-4M24 16v-6" stroke="#fff" stroke-width="2"/><rect x="24" y="22" width="10" height="13" rx="1" fill="#fff"/></svg></div><div class="svc-name">RECONCILE<br>GENERAL LEDGER<br>ACCOUNTS</div></div>
    <div class="svc" style="left:105px;top:545px"><div class="svc-icon"><svg width="40" height="40" viewBox="0 0 40 40"><path d="M9 4h16l6 6v26H9z" fill="none" stroke="#fff" stroke-width="2"/><path d="M14 14h12M14 20h12" stroke="#fff" stroke-width="2"/><text x="12" y="34" font-family="Montserrat,sans-serif" font-size="13" font-weight="700" fill="#fff">$</text></svg></div><div class="svc-name">PREPARE &amp; INTERPRET<br>FINANCIAL STATEMENTS</div></div>
    <div class="foot foot--teal">WWW.PRODUCERLEDGERBOOKS.COM</div>
    <div class="foot-base" style="background:#fff"></div>
  </div>

  <div class="panel panel--c panel--teal">
    <div class="tab tab--white" style="left:0;top:24px">HOW THE CPLR FEES ARE STRUCTURED</div>
    <div class="fees-body">
      <p class="fees-text">Fees are a flat monthly rate based on annual policy commission revenue. The table below lists sample rates for our full-service offerings at different revenue volumes for an Agency with a typical mix of business and complexity. Fees assume compliance with our standard operating workflows. Fees are updated annually and 60 days’ notice is provided.</p>
      <table class="fee-table">
        <thead><tr><th>Annual Commission<br>Revenue</th><th>Monthly Service<br>Fee</th></tr></thead>
        <tbody>
          <tr><td>&lt;$300,000</td><td>$600</td></tr>
          <tr><td>$700,000</td><td>$1,500</td></tr>
          <tr><td>$1,000,000</td><td>$2,200</td></tr>
          <tr><td>$1,500,000</td><td>$2,700</td></tr>
          <tr><td>$2,000,000</td><td>$3,200</td></tr>
          <tr><td>$2,500,000</td><td>$3,800</td></tr>
          <tr><td>$3,000,000</td><td>$4,800</td></tr>
          <tr><td>$3,500,000</td><td>$5,800</td></tr>
          <tr><td>$4,000,000</td><td>$6,700</td></tr>
        </tbody>
      </table>
      <p class="fees-more">We can provide services for larger agencies, typically supplementing in-house staff.</p>
    </div>
    <div class="photo" role="img" aria-label="Two colleagues reviewing work on a laptop in a bright office" style="left:0;top:455px;width:334px;height:266px;background:linear-gradient(180deg,#0d8b80 0%,#7fb9b8 25%,#c9d6dc 55%,#e9ecef 100%)"></div>
    <svg class="abs" style="left:0;top:640px" width="334" height="95" viewBox="0 0 334 95"><path d="M0 60 Q90 10 180 45 T334 20 V95 H0Z" fill="#b5b5b5"/><path d="M0 55 Q90 5 180 40 T334 15" fill="none" stroke="#00BBA5" stroke-width="4"/></svg>
    <div class="foot">WWW.PRODUCERLEDGERBOOKS.COM</div>
    <div class="foot-base"></div>
  </div>
</section>

<div class="map-title">Tri-Fold Panels</div>
<div class="map" style="left:155px">
  <div>5<br>OUTER<br>FLAP</div>
  <div>6<br>BACK<br>COVER</div>
  <div>1<br>FRONT<br>COVER</div>
</div>
<div class="map" style="left:586px">
  <div>2<br>INNER<br>FRONT</div>
  <div>3<br>INNER<br>CENTER</div>
  <div>4<br>INNER<br>FLAP</div>
</div>

</body>
</html>
```